Keystead Insurance Provider Website

We are selling Keystead Insurance policy / tenants Policy/Flood Insurance in USA in few states and planning expand nationally.

Our target audience are two folds: Customers (Buy policies) and Insurance Agents who wants to work with us to sell our policies to customers. But website should focus 80% on customers and 20% on agents. So, more customer focused user experience. Please note that there is no direct buy option for customers. They always go through insurance agents.

Customer focused, educational that makes buyer journey easy. We don’t want to come off as trying sell something as there is no direct sales involved from website.

Target Market(s)

Homeowners in USA and Insurance agent who sells these insurance.

Industry/Entity Type

Insurance

Number of Pages Required

4 page

Font styles to use
Other font styles liked:
• Open to suggestions

Colors

Designer to choose colors to be used in the design.

Requirements
Must have
• Three most important things: Trustworthy, Authentic, Simple
• Please use colors form logo and grays
• We like: www.harborlane.com
• https://www.veltrimoor.com/
• We need Agent Look up tool on home page similar to what is shown on example sites.
• Design:
• Home Page - Open to Ideas
• Insurance (Products) Landing Page - Info similar to: https://www.veltrimoor.com/insurance/
• Agents Page - https://www.veltrimoor.com/agents/
• Claims Page - Information similar to: https://www.veltrimoor.com/claims-center/
• Site Navigation:
• Home
• Insurance
• Claims
• Agents
• About Us
• Contact Us
Nice to have
• Elegant, minimal and clean design that reflects trust and authenticity.
Should not have
• Slider or rotating images - prefer flat design. Not over powering design.

```html
<!DOCTYPE html>
<html lang="en">
<head>
<meta charset="utf-8">
<title>Keystead Insurance Co. — Find an Agent</title>
<link href="https://fonts.googleapis.com/css2?family=Montserrat:wght@500;600&family=Source+Sans+3:wght@400;600;700&display=swap" rel="stylesheet">
<style>
:root{
  --navy:#1b3e8e;
  --navy-deep:#142f70;
  --red:#d2202c;
  --red-dark:#a8151f;
  --ink:#2e3138;
  --text:#555a63;
  --muted:#6d727b;
  --line:#d9dce1;
  --footer:#363b44;
  --footer-text:#c5c9d0;
  --white:#ffffff;
}
*{box-sizing:border-box;margin:0;padding:0}
html,body{width:785px;height:1200px;overflow:hidden}
body{position:relative;font-family:"Source Sans 3",Arial,sans-serif;color:var(--ink);background:var(--white)}
.abs{position:absolute}

/* header */
.site-header{left:0;top:0;width:785px;height:49px;background:var(--white);z-index:5}
.brand{display:flex;align-items:center;gap:7px;color:var(--navy);font-weight:600;text-transform:uppercase;line-height:1}
.brand-mark{width:22px;height:22px;background:var(--navy)}
.brand-name{font-size:13px;letter-spacing:.2px}
.brand-name small{display:block;font-size:9px;letter-spacing:2.4px;margin-top:2px}
.site-header .brand{left:112px;top:10px}
.main-nav{left:290px;top:18px;display:flex;gap:12px;font-size:8.6px;font-weight:600}
.main-nav a{color:var(--text);text-decoration:none}
.main-nav a.active{color:var(--red)}
.btn{display:inline-flex;align-items:center;justify-content:center;gap:4px;color:var(--white);font-weight:700;border-radius:2px;text-decoration:none}
.btn-careers{left:556px;top:14px;width:56px;height:20px;background:var(--navy);font-size:8.6px}
.btn-login{left:615px;top:14px;width:57px;height:20px;background:var(--red);font-size:8.6px}

/* hero */
.hero{left:0;top:49px;width:785px;height:294px;background:linear-gradient(90deg,#f3f4f6 0%,#eceef1 45%,#e4e6ea 100%)}
.hero-photo{left:400px;top:49px;width:385px;height:294px;background:radial-gradient(ellipse at 55% 45%,#d8c0ae 0%,#cfd2d6 40%,#e1e3e6 75%,#eceef1 100%)}
.hero-title{left:112px;top:114px;font-family:Montserrat,Arial,sans-serif;font-weight:500;font-size:18px;color:#1e2126}
.hero-lead{left:113px;top:140px;width:270px;font-size:9.3px;line-height:14.5px;color:var(--text)}
.agent-search{left:113px;top:185px;width:194px;height:31px;background:var(--white);border:1px solid var(--line);display:flex;align-items:center;padding:2px}
.agent-search span{flex:1;font-size:8px;color:#8a8f97;padding-left:8px}
.btn-find{height:25px;padding:0 10px;background:var(--red);font-size:9px;font-weight:600}

/* product circles */
.products{left:0;top:343px;width:785px;height:178px;background:linear-gradient(180deg,#ffffff 0%,#f7f8f9 60%,#eef0f2 100%)}
.product{width:116px;height:116px;border-radius:50%;background:var(--white);display:flex;align-items:center;justify-content:center;top:283px;z-index:3}
.product-inner{width:106px;height:106px;border-radius:50%;background:radial-gradient(circle at 50% 35%,#2456b0 0%,var(--navy) 55%,var(--navy-deep) 100%);display:flex;flex-direction:column;align-items:center;justify-content:center;color:var(--white);font-size:8.6px;font-weight:600;text-align:center;line-height:10px;gap:6px}
.product svg{width:34px;height:34px}

.claim-note{left:0;top:422px;width:785px;text-align:center;font-size:11.4px;line-height:15px;color:var(--ink);z-index:3}
.claim-note em{font-style:normal;color:var(--red)}
.btn-claim{left:336px;top:464px;width:112px;height:32px;background:var(--red);border-bottom:2px solid var(--red-dark);font-size:11px;letter-spacing:.2px;z-index:3}

/* feature rows */
.feature-photo{width:393px;height:245px}
.photo-family{left:0;top:521px;background:linear-gradient(120deg,#d6cfc4 0%,#b99c86 40%,#8fa7ad 70%,#c6c8c7 100%)}
.photo-support{left:392px;top:766px;background:linear-gradient(110deg,#c8ccd2 0%,#d9d2cb 45%,#eef0f3 75%,#b4bcc8 100%)}
.feature-copy{width:245px}
.feature-copy h2{font-weight:400;font-size:14.2px;line-height:17px;color:#2a2d33;margin-bottom:12px}
.feature-copy p{font-size:7.1px;line-height:12.8px;color:var(--muted)}
.copy-one{left:431px;top:557px}
.copy-two{left:112px;top:802px}

/* footer */
.site-footer{left:0;top:1011px;width:785px;height:189px;background:var(--footer);color:var(--footer-text)}
.site-footer .brand{left:112px;top:1026px;color:var(--white)}
.site-footer .brand-mark{background:var(--white)}
.footer-phone{left:112px;top:1068px;font-size:11px;color:var(--white)}
.footer-mail{left:112px;top:1082px;font-size:7.6px}
.socials{left:113px;top:1102px;display:flex;gap:4px}
.socials span{width:19px;height:19px;border-radius:50%;border:1.2px solid var(--footer-text)}
.footer-col h3{font-size:9px;font-weight:600;color:var(--white);margin-bottom:7px}
.footer-col a{display:block;font-size:7.4px;line-height:12.8px;color:var(--footer-text);text-decoration:none}
.col-company{left:256px;top:1035px}
.col-login{left:351px;top:1035px}
.col-support{left:480px;top:1035px}
.col-connect{left:590px;top:1035px}
.btn-footer-find{left:352px;top:1091px;width:92px;height:26px;background:var(--red);font-size:9px;font-weight:600}
.legal{left:0;top:1147px;width:785px;text-align:center;font-size:7.2px;line-height:12.8px}
</style>
</head>
<body>

<header class="site-header abs">
  <div class="brand abs"><span class="brand-mark"></span><span class="brand-name">Keystead<small>Insurance Co.</small></span></div>
  <nav class="main-nav abs">
    <a class="active" href="#">Home</a><a href="#">Insurance</a><a href="#">About Us</a><a href="#">Claims</a><a href="#">Agents</a><a href="#">Contact Us</a>
  </nav>
  <a class="btn btn-careers abs" href="#"><svg width="7" height="8" viewBox="0 0 7 8"><circle cx="3.5" cy="2" r="2" fill="#fff"/><path d="M0 8c0-2.5 1.5-3.5 3.5-3.5S7 5.5 7 8z" fill="#fff"/></svg>Careers</a>
  <a class="btn btn-login abs" href="#"><svg width="7" height="8" viewBox="0 0 7 8"><rect x="0" y="3.5" width="7" height="4.5" fill="#fff"/><path d="M1.5 3.5V2.3a2 2 0 0 1 4 0v1.2" stroke="#fff" fill="none"/></svg>Login</a>
</header>

<section class="hero abs"></section>
<div class="hero-photo abs" role="img" aria-label="Smiling woman holding a tablet in a bright office"></div>
<h1 class="hero-title abs">Find an Agent</h1>
<p class="hero-lead abs">Talk to one of our local independent agencies to get a quote, ask questions about coverage options &amp; more!</p>
<form class="agent-search abs">
  <span>ZIP Code</span>
  <a class="btn btn-find" href="#"><svg width="11" height="11" viewBox="0 0 12 12"><circle cx="5" cy="5" r="4" stroke="#fff" stroke-width="1.4" fill="none"/><path d="M8 8l3 3" stroke="#fff" stroke-width="1.4"/></svg>Find an Agent</a>
</form>

<section class="products abs"></section>

<a class="product abs" style="left:119px" href="#"><span class="product-inner">
  <svg viewBox="0 0 34 34"><path d="M4 17L17 5l13 12" stroke="#fff" stroke-width="3" fill="none"/><path d="M8 16v13h7v-8h4v8h7V16L17 8z" fill="#fff"/></svg>Homeowners</span></a>
<a class="product abs" style="left:263px" href="#"><span class="product-inner">
  <svg viewBox="0 0 34 34"><rect x="8" y="3" width="18" height="28" fill="#fff"/><g fill="#1b3e8e"><rect x="11" y="7" width="3" height="3"/><rect x="15.5" y="7" width="3" height="3"/><rect x="20" y="7" width="3" height="3"/><rect x="11" y="13" width="3" height="3"/><rect x="15.5" y="13" width="3" height="3"/><rect x="20" y="13" width="3" height="3"/><rect x="11" y="19" width="3" height="3"/><rect x="15.5" y="19" width="3" height="3"/><rect x="20" y="19" width="3" height="3"/><rect x="15" y="25" width="4" height="6"/></g></svg>Renters/Condo</span></a>
<a class="product abs" style="left:406px" href="#"><span class="product-inner">
  <svg viewBox="0 0 34 34"><path d="M2 17L14 6l8 7" stroke="#fff" stroke-width="3" fill="none"/><path d="M5 16v13h16V14l-7-6z" fill="#fff"/><rect x="9" y="18" width="7" height="6" fill="#1b3e8e"/><path d="M26 30c-4 0-6-3-5-7 1-3 3-4 3-8 3 2 4 5 3 8 1-1 2-2 2-4 2 3 3 5 2 8-1 2-3 3-5 3z" fill="#fff"/></svg>Dwelling Fire</span></a>
<a class="product abs" style="left:550px" href="#"><span class="product-inner">
  <svg viewBox="0 0 34 34"><path d="M17 3a8 8 0 0 0-8 8c0 6 8 14 8 14s8-8 8-14a8 8 0 0 0-8-8z" fill="#fff"/><circle cx="17" cy="11" r="3" fill="#1b3e8e"/><path d="M8 22l-5 9h28l-5-9" stroke="#fff" stroke-width="2" fill="none"/></svg>Agent Locator<br>Tool</span></a>

<p class="claim-note abs">To make it easy and stress free as possible, we have quick online form for you to report<br>a claim or you can call us at <em>1-866-555-0142</em></p>
<a class="btn btn-claim abs" href="#">REPORT A CLAIM</a>

<div class="feature-photo photo-family abs" role="img" aria-label="Family of four with their dog sitting together on a sofa at home"></div>
<article class="feature-copy copy-one abs">
  <h2>Professional lorem ipsum generator for typographers</h2>
  <p>Morbi accumsan ipsum velit. Nam nec tellus a odio tincidunt auctor a ornare odio. Sed non mauris vitae erat consequat auctor eu in elit. Class aptent taciti sociosqu ad litora torquent per conubia nostra, per inceptos himenaeos. Mauris in erat justo. Nullam ac urna eu felis dapibus neque condimentum sit amet a augue. Sed non neque elit. Sed ut imperdiet nisi. Proin condimentum fermentum nunc. Etiam pharetra, erat sed useded fermentum feugiat, velit mauris egestas quam, ut aliquam massa nisl quis neque. Suspendisse in orci enim.</p>
</article>

<article class="feature-copy copy-two abs">
  <h2>Professional lorem ipsum generator for typographers</h2>
  <p>Morbi accumsan ipsum velit. Nam nec tellus a odio tincidunt auctor a ornare odio. Sed non mauris vitae erat consequat auctor eu in elit. Class aptent taciti sociosqu ad litora torquent per conubia nostra, per inceptos himenaeos. Mauris in erat justo. Nullam ac urna eu felis dapibus neque condimentum sit amet a augue. Sed non neque elit. Sed ut imperdiet nisi. Proin condimentum fermentum nunc. Etiam pharetra, erat sed useded fermentum feugiat, velit mauris egestas quam, ut aliquam massa nisl quis neque. Suspendisse in orci enim.</p>
</article>
<div class="feature-photo photo-support abs" role="img" aria-label="Customer support team wearing headsets at their desks"></div>

<footer class="site-footer abs"></footer>
<div class="site-footer-content">
  <div class="brand abs" style="left:112px;top:1026px;color:#fff"><span class="brand-mark" style="background:#fff"></span><span class="brand-name">Keystead<small>Insurance Co.</small></span></div>
  <div class="footer-phone abs">1 800 555 0199</div>
  <div class="footer-mail abs">info@keysteadinsurance.co</div>
  <div class="socials abs" aria-label="Social links"><span></span><span></span><span></span><span></span></div>
  <div class="footer-col col-company abs"><h3>Our Company</h3><a href="#">Home</a><a href="#">Insurance</a><a href="#">About Us</a><a href="#">Claims</a><a href="#">Agents</a></div>
  <div class="footer-col col-login abs"><h3>Login to Your Account</h3><a href="#">Agents Login</a><a href="#">Clients login</a></div>
  <a class="btn btn-footer-find abs" href="#"><svg width="11" height="11" viewBox="0 0 12 12"><circle cx="5" cy="5" r="4" stroke="#fff" stroke-width="1.4" fill="none"/><path d="M8 8l3 3" stroke="#fff" stroke-width="1.4"/></svg>Find an Agent</a>
  <div class="footer-col col-support abs"><h3>Customer Support</h3><a href="#">FAQs</a><a href="#">Resources</a><a href="#">Report a Claim</a><a href="#">Find an Agent</a></div>
  <div class="footer-col col-connect abs"><h3>Connect With Us</h3><a href="#">Support</a><a href="#">Careers</a></div>
  <div class="legal abs" style="color:#c5c9d0">Copyright ©2018 Keystead Insurance. All Rights Reserved<br>Terms of Use &nbsp;-&nbsp; Privacy Policy &nbsp;-&nbsp; Sitemap</div>
</div>

</body>
</html>
```